modern real estate design
business card/letterhead/envelop
Dorian Parks
President
408 W Birch Avenue Elm Ridge, ND 56093
dorian@tidewaterhomesgroup.com
www.tidewaterhomesgroup.com
Licensed Realtor with Quiet Harbor Real Estate
Find Your Harbor.
newell343 newell343
I am also interested in getting a design done for metal business cards. It would be cool to have them die cut, etched, and have our two color logo on them. Thanks.

```html
<!DOCTYPE html>
<html lang="en">
<head>
<meta charset="utf-8">
<title>Tidewater Homes Group – Business Card</title>
<link rel="stylesheet" href="https://fonts.googleapis.com/css2?family=Roboto:wght@300;400;500&display=swap">
<style>
  :root {
    --backdrop: #2a2a2c;
    --card-top: #1c1c1e;
    --card-bottom: #0b0b0c;
    --teal: #2fb6c8;
    --white: #f2f2f2;
    --grey: #a7a9ac;
    --silver-light: #e6e7e9;
    --silver-dark: #7d8086;
  }
  * { margin: 0; padding: 0; box-sizing: border-box; }
  html, body {
    width: 1200px; height: 751px; overflow: hidden;
    background: var(--backdrop);
    font-family: "Roboto", Arial, sans-serif;
  }
  .canvas { position: relative; width: 1200px; height: 751px; }

  .card {
    position: absolute;
    width: 540px; height: 310px;
    background: linear-gradient(160deg, var(--card-top), var(--card-bottom));
    overflow: hidden;
    box-shadow: 0 14px 30px rgba(0,0,0,.45);
  }
  .card-front { left: 60px; top: 70px; border-radius: 155px 6px 6px 155px; }
  .card-back { left: 600px; top: 370px; border-radius: 6px 155px 6px 6px; }

  .crescent { position: absolute; top: 0; display: block; }
  .card-front .crescent { left: 0; }
  .card-back .crescent { right: 0; }

  .brand {
    position: absolute; left: 205px; top: 116px;
    display: flex; align-items: center; gap: 10px;
    white-space: nowrap;
  }
  .brand-dot {
    width: 14px; height: 14px; border-radius: 50%;
    background: var(--teal); flex: none;
  }
  .brand-name {
    font-weight: 500; font-size: 18px; letter-spacing: 1.5px;
    color: var(--white); text-transform: uppercase; line-height: 1;
  }
  .tagline {
    position: absolute; right: 32px; top: 160px;
    font-weight: 300; font-size: 24px; color: var(--white);
    white-space: nowrap;
  }

  .contact { position: absolute; left: 34px; top: 118px; }
  .name { font-weight: 400; font-size: 19px; color: var(--teal); }
  .role { font-weight: 300; font-size: 11px; color: var(--grey); margin-top: 2px; }
  .address {
    font-weight: 300; font-size: 11px; color: var(--grey);
    margin-top: 14px; line-height: 1.45; font-style: normal;
  }
  .lines { list-style: none; margin-top: 12px; }
  .lines li {
    display: flex; align-items: center; gap: 8px;
    font-weight: 300; font-size: 11px; color: var(--grey);
    line-height: 1.9; white-space: nowrap;
  }
  .icon { width: 11px; height: 11px; flex: none; }
  .licence {
    position: absolute; left: 34px; bottom: 16px;
    font-weight: 300; font-size: 9px; color: var(--silver-dark);
  }
</style>
</head>
<body>
<main class="canvas">

  <section class="card card-front" aria-label="Card front">
    <svg class="crescent" width="170" height="310" viewBox="0 0 170 310" role="img" aria-label="Silver cratered moon crescent texture">
      <defs>
        <linearGradient id="silver-front" x1="0" y1="0" x2="1" y2="1">
          <stop offset="0" stop-color="#e6e7e9"/>
          <stop offset="1" stop-color="#7d8086"/>
        </linearGradient>
        <mask id="crescent-front">
          <rect width="170" height="310" fill="#fff"/>
          <circle cx="210" cy="155" r="168" fill="#000"/>
        </mask>
      </defs>
      <circle cx="155" cy="155" r="155" fill="url(#silver-front)" mask="url(#crescent-front)"/>
    </svg>
    <div class="brand">
      <span class="brand-dot"></span>
      <span class="brand-name">Tidewater Homes Group</span>
    </div>
    <p class="tagline">Find Your Harbor.</p>
  </section>

  <section class="card card-back" aria-label="Card back">
    <svg class="crescent" width="300" height="120" viewBox="0 0 300 120" role="img" aria-label="Silver cratered moon crescent texture">
      <defs>
        <linearGradient id="silver-back" x1="0" y1="0" x2="1" y2="1">
          <stop offset="0" stop-color="#e6e7e9"/>
          <stop offset="1" stop-color="#7d8086"/>
        </linearGradient>
        <mask id="crescent-back">
          <rect width="300" height="120" fill="#fff"/>
          <circle cx="150" cy="195" r="170" fill="#000"/>
        </mask>
      </defs>
      <circle cx="150" cy="150" r="150" fill="url(#silver-back)" mask="url(#crescent-back)"/>
    </svg>

    <div class="contact">
      <h1 class="name">Dorian Parks</h1>
      <p class="role">President</p>
      <address class="address">408 W Birch Avenue<br>Elm Ridge, ND 56093</address>
      <ul class="lines">
        <li>
          <svg class="icon" viewBox="0 0 12 12"><rect x="3" y="0.5" width="6" height="11" rx="1.2" fill="#2fb6c8"/><rect x="4.3" y="2" width="3.4" height="6.5" fill="#111"/></svg>
          612-555-0148
        </li>
        <li>
          <svg class="icon" viewBox="0 0 12 12"><rect x="0.5" y="2" width="11" height="8" rx="1" fill="#2fb6c8"/><path d="M1 2.6 6 6.6 11 2.6" stroke="#111" stroke-width="1" fill="none"/></svg>
          dorian@tidewaterhomesgroup.com
        </li>
        <li>
          <svg class="icon" viewBox="0 0 12 12"><circle cx="6" cy="6" r="5.3" fill="#2fb6c8"/><path d="M1 6h10M6 .8c-2.4 2.8-2.4 7.6 0 10.4M6 .8c2.4 2.8 2.4 7.6 0 10.4" stroke="#111" stroke-width=".8" fill="none"/></svg>
          www.tidewaterhomesgroup.com
        </li>
      </ul>
    </div>
    <p class="licence">Licensed Realtor with Quiet Harbor Real Estate</p>
  </section>

</main>
</body>
</html>
```